Thriving Mexican import business needs a new business card

Need a refresher of our current business card. Looking for a lighter background with the logo on one side. We will want this file to be adjustable so we can change names, emails and mobile numbers.
We are open to ideas but maintaining a professional image is critical.
Thankyou,

Target Market(s)

Anyone in food industry

Industry/Entity Type

Wholesale

Contact Information for Business Card

Mark Pendlebury
Director
Condor Provisions & Spirits Pty Ltd
5B Morrow Ct, Kelvinbrook VIC 3127
0421930576 (03) 95128460
mark@condorlatino.example.au
condorlatinoprovisionsandspirits.example.au

Font styles to use
Serif
Other font styles liked:
• NeoGram Heavy

Requirements
Must have
• Professional yet memorable
Condor logo
Nice to have
• Chilli or tequila/mexican food pictures
Should not have
• Dark background

```html
<!DOCTYPE html>
<html lang="en">
<head>
<meta charset="utf-8">
<title>Condor Provisions &amp; Spirits – Business Card</title>
<link rel="stylesheet" href="https://fonts.googleapis.com/css2?family=Oswald:wght@700&family=Questrial&display=swap">
<style>
  :root {
    --stage: #3b3c3e;
    --card-light: #e9ebee;
    --ink: #1c1c1c;
    --rule: #4a4a4a;
    --card-dark: #111111;
    --brick: #1b1b1b;
    --silver: #d4d6d9;
    --frame: #c9cbce;
  }
  * { box-sizing: border-box; margin: 0; padding: 0; }
  html, body { width: 1200px; height: 1000px; overflow: hidden; }
  body {
    background: var(--stage);
    position: relative;
    font-family: "Questrial", "Century Gothic", sans-serif;
    color: var(--ink);
  }
  .card {
    position: absolute;
    width: 640px;
    height: 370px;
    border-radius: 28px;
    overflow: hidden;
  }

  /* Front */
  .card-front {
    left: 70px; top: 80px;
    background: var(--card-light);
    display: flex;
    align-items: center;
    padding: 0 36px 0 40px;
  }
  .brand-block {
    flex: none;
    width: 270px;
    display: flex;
    align-items: center;
    justify-content: center;
    gap: 12px;
    overflow: hidden;
  }
  .brand-mark {
    width: 16px; height: 16px;
    background: var(--ink);
    flex: none;
  }
  .brand-name {
    font-family: "Oswald", "Arial Narrow", sans-serif;
    font-weight: 700;
    font-size: 56px;
    letter-spacing: 1px;
    line-height: 1;
    text-transform: uppercase;
    color: var(--ink);
    white-space: nowrap;
  }
  .divider {
    flex: none;
    width: 1px;
    height: 250px;
    background: var(--rule);
    margin: 0 22px 0 16px;
  }
  .contact-block { flex: 1; min-width: 0; font-weight: 700; }
  .person-name {
    font-size: 18px;
    letter-spacing: 1px;
    text-transform: uppercase;
    white-space: nowrap;
  }
  .person-role {
    font-size: 12px;
    letter-spacing: 1px;
    text-transform: uppercase;
    margin-top: 4px;
  }
  .contact-list { list-style: none; margin-top: 26px; }
  .contact-list li {
    display: flex;
    align-items: center;
    gap: 8px;
    font-size: 13.5px;
    line-height: 1;
    margin-bottom: 10px;
    white-space: nowrap;
  }
  .contact-icon { width: 16px; height: 16px; flex: none; }
  .address {
    font-style: normal;
    font-size: 13px;
    line-height: 1.35;
    margin-top: 18px;
    white-space: nowrap;
  }

  /* Back */
  .card-back {
    left: 490px; top: 540px;
    background: var(--card-dark);
  }
  .back-texture {
    position: absolute; inset: 0;
    background: linear-gradient(160deg, #1e1e1e, var(--brick) 55%, #141414);
  }
  .back-frame {
    position: absolute;
    inset: 22px;
    border: 1.5px solid var(--frame);
    border-radius: 10px;
    display: flex;
    flex-direction: column;
    align-items: center;
    justify-content: center;
    gap: 34px;
  }
  .back-brand {
    display: flex; align-items: center; gap: 16px;
  }
  .back-brand .brand-mark { background: var(--silver); width: 22px; height: 22px; }
  .back-brand .brand-name { color: var(--silver); font-size: 96px; }
  .website {
    font-size: 21px;
    font-weight: 700;
    color: var(--silver);
    letter-spacing: 0.3px;
    white-space: nowrap;
  }
</style>
</head>
<body>

  <section class="card card-front" aria-label="Business card front">
    <div class="brand-block">
      <span class="brand-mark"></span>
      <span class="brand-name">Condor</span>
    </div>
    <div class="divider"></div>
    <div class="contact-block">
      <p class="person-name">Mark Pendlebury</p>
      <p class="person-role">Director</p>
      <ul class="contact-list">
        <li>
          <svg class="contact-icon" viewBox="0 0 16 16" aria-hidden="true"><rect width="16" height="16" rx="3" fill="#1c1c1c"/><rect x="5" y="3" width="6" height="10" rx="1" fill="none" stroke="#e9ebee" stroke-width="1.4"/></svg>
          0421930576
        </li>
        <li>
          <svg class="contact-icon" viewBox="0 0 16 16" aria-hidden="true"><rect width="16" height="16" rx="3" fill="#1c1c1c"/><path d="M4 7c0-2 8-2 8 0v1H4z M5 9h6v3H5z" fill="#e9ebee"/></svg>
          (03) 95128460
        </li>
        <li>
          <svg class="contact-icon" viewBox="0 0 16 16" aria-hidden="true"><rect width="16" height="16" rx="3" fill="#1c1c1c"/><rect x="3" y="5" width="10" height="7" fill="none" stroke="#e9ebee" stroke-width="1.3"/><path d="M3 5l5 4 5-4" fill="none" stroke="#e9ebee" stroke-width="1.3"/></svg>
          mark@condorlatino.example.au
        </li>
      </ul>
      <address class="address">
        Condor Provisions &amp; Spirits Pty Ltd<br>
        5B Morrow Ct, Kelvinbrook<br>
        VIC 3127
      </address>
    </div>
  </section>

  <section class="card card-back" aria-label="Business card back">
    <div class="back-texture" role="img" aria-label="Dark brick wall texture"></div>
    <div class="back-frame">
      <div class="back-brand">
        <span class="brand-mark"></span>
        <span class="brand-name">Condor</span>
      </div>
      <p class="website">condorlatinoprovisionsandspirits.example.au</p>
    </div>
  </section>

</body>
</html>
```